Protein Powder Bag Design

We need a packaging design for a protein powder for our supplement company. The company is "Dawn Hollow" and the product is called "SUMMIT PROTEIN"

The bag design needs to include:

- Our Logo
- Grass-Fed Beef Isolate Powder
- Chocolate (as the flavor)
- 2lbs 900grams Dietary Supplement
- Matte finish

The back of the bag needs to include:

- Blurb about Dawn Hollow
i.e. Live Dawn Hollow for anything and part of that means dialing in your nutrition. We are about clean, real, whole foods, quality, transparency, health, performance, flexible lifestyle, convenience, paleo friendly, no gluten

- Supplement Facts (attached)
*Under Supplement Facts*
INGREDIENTS: Grass-Fed Beef Protein (CattlePRO TM), Cocoa Powder, Stevia Leaf Powder

- Barcode (attached)
- #eatrealfood
- info@dawnhollowfoods.example
- dawnhollowfoods.example
- Manufactured for Dawn Hollow, San Francisco, Ca 94107
- Collagen/Gellatin
- Complete source of protein
- Free from: dairy, gluten, whey, soy, antibiotics, hormones, fillers, artificial sweeteners, preservatives, and other nonsense.

- Suggested Use:
Mix with 8 to 10 oz of liquid or add to baked foods to feel amazing. Store in a dry, cool place.

- Ingredients Per Scoop:
4 oz grass-fed beef
Cocoa Powder
Stevia

- **These statements have not been evaluated by The Board of Nutrient Oversight. This product is not intended to diagnose, treat, cure or prevent disease.

• - Matte finish
• - Blue, white, color scheme
• - Check out the templates (do not copy)

```html
<!DOCTYPE html>
<html lang="en">
<head>
<meta charset="utf-8">
<title>Summit Protein – Chocolate Pouch Front</title>
<link rel="stylesheet" href="https://fonts.googleapis.com/css2?family=Oswald:wght@300;400;500&family=Yanone+Kaffeesatz:wght@300;400&display=swap">
<style>
  :root {
    --page: #ffffff;
    --pouch-black: #141414;
    --blue-deep: #1d78bd;
    --blue-light: #45aee3;
    --cocoa: #5b4033;
    --cocoa-dark: #3a2822;
    --cocoa-light: #a6755a;
    --ink-light: #e9ecee;
    --ink-white: #ffffff;
    --rule: rgba(255,255,255,0.55);
  }
  * { box-sizing: border-box; margin: 0; padding: 0; }
  html, body {
    width: 1200px; height: 1200px; overflow: hidden;
    background: var(--page);
  }
  .pouch-front {
    position: absolute;
    left: 210px; top: 60px;
    width: 780px; height: 1080px;
    background: var(--pouch-black);
    border-radius: 14px;
    overflow: hidden;
    font-family: "Oswald", sans-serif;
    color: var(--ink-light);
  }
  .brand {
    position: absolute; left: 0; right: 0; top: 190px;
    text-align: center;
  }
  .brand-name {
    font-family: "Oswald", sans-serif;
    font-weight: 300;
    font-size: 40px;
    letter-spacing: 0.32em;
    color: var(--ink-white);
    padding-left: 0.32em;
  }
  .label-band {
    position: absolute; left: 0; right: 0; top: 332px; height: 510px;
    background: linear-gradient(90deg, var(--blue-deep) 0%, #2d92d2 55%, var(--blue-light) 100%);
  }
  .product-art {
    position: absolute; left: 350px; top: 0; width: 430px; height: 510px;
    background:
      radial-gradient(ellipse 60% 35% at 78% 14%, var(--cocoa-light) 0%, rgba(166,117,90,0.6) 45%, rgba(166,117,90,0) 80%),
      radial-gradient(ellipse 55% 55% at 45% 55%, rgba(255,255,255,0.18) 0%, rgba(255,255,255,0) 70%);
  }
  .product-title {
    position: absolute; left: 92px; top: 40px;
    font-family: "Oswald", sans-serif;
    font-weight: 400;
    font-size: 104px;
    line-height: 0.98;
    letter-spacing: -0.01em;
    color: var(--ink-light);
    transform: scaleX(0.86);
    transform-origin: left top;
  }
  .rule {
    position: absolute; left: 80px; width: 255px; height: 2px;
    background: var(--rule);
  }
  .rule.top { top: 286px; }
  .rule.bottom { top: 496px; }
  .product-type {
    position: absolute; left: 94px; top: 294px;
    font-family: "Yanone Kaffeesatz", sans-serif;
    font-weight: 400;
    font-size: 52px;
    line-height: 49px;
    color: var(--ink-light);
  }
  .flavor-badge {
    position: absolute; left: 540px; top: 600px; width: 190px; height: 190px;
  }
  .flavor-text {
    position: absolute; left: 554px; top: 665px; width: 158px;
    text-align: center;
    font-family: "Yanone Kaffeesatz", sans-serif;
    color: var(--ink-white);
    line-height: 1;
  }
  .flavor-text .label { display: block; font-size: 30px; font-weight: 300; }
  .flavor-text .name { display: block; font-size: 50px; font-weight: 400; margin-top: 2px; }
  .size-band {
    position: absolute; left: 0; right: 0; top: 842px; height: 110px;
    background: linear-gradient(180deg, var(--cocoa) 0%, var(--cocoa-dark) 55%, var(--pouch-black) 100%);
  }
  .size-line {
    position: absolute; left: 0; right: 0; top: 884px;
    text-align: center;
    font-family: "Oswald", sans-serif;
    color: var(--ink-white);
    letter-spacing: 0.04em;
  }
  .size-line .weight { font-size: 26px; font-weight: 500; }
  .size-line .kind { font-size: 17px; font-weight: 500; margin-left: 8px; }
</style>
</head>
<body>
  <main class="pouch-front">
    <div class="brand">
      <span class="brand-name">DAWN HOLLOW</span>
    </div>

    <section class="label-band">
      <div class="product-art" role="img" aria-label="Line drawing of a cow's head with chocolate pieces and cocoa powder"></div>
      <h1 class="product-title">SUMMIT<br>PROTEIN</h1>
      <div class="rule top"></div>
      <p class="product-type">GRASS-FED<br>BEEF<br>ISOLATE<br>POWDER</p>
      <div class="rule bottom"></div>
    </section>

    <svg class="flavor-badge" viewBox="0 0 190 190" aria-hidden="true">
      <polygon points="38,18 40,70 82,48" fill="#5b4033"/>
      <circle cx="104" cy="104" r="80" fill="#5b4033"/>
    </svg>
    <p class="flavor-text"><span class="label">flavor</span><span class="name">Chocolate</span></p>

    <div class="size-band"></div>
    <p class="size-line"><span class="weight">2LBS 900GRAMS</span><span class="kind">DIETARY SUPPLEMENT</span></p>
  </main>
</body>
</html>
```